Networking Events Calendar/Diary

We need a responsive website that can act as both an online diary/calendar and a resource for community and networking events similar to lookupmixerdates.com (we do not want a clone, but one with similar functionality). We need to be able to host adverts, have a client area for clients to add their own events to the diary. This needs to have the functionality that clients have to pay to add recurring events. Some integration would be useful so that if a clients already has their own online diary on their website then using an API possibly to also add that event into our online diary

Industry/Entity Type

Events

Coding

Coded - Design and coding required

Number of Pages Required

5+ page

Requirements
Must have
• My project must have a calendar area, space for ads, be responsive and easily viewable on mobile. A subscribers area for clients and a way to purchase premium status so that premium events are highlighted.

```html
<!DOCTYPE html>
<html lang="en">
<head>
<meta charset="utf-8">
<title>Kestrel Events — Networking Events Diary</title>
<link href="https://fonts.googleapis.com/css2?family=Open+Sans:wght@400;600;700&family=Montserrat:wght@400;600;700&display=swap" rel="stylesheet">
<style>
:root{
  --navy:#1c3f67;
  --navy-dark:#15304f;
  --navy-deep:#10253d;
  --orange:#f6a11a;
  --ink:#222;
  --text:#6b6b6b;
  --line:#e3e3e3;
  --white:#fff;
}
*{box-sizing:border-box;margin:0;padding:0}
html,body{width:1200px;height:3696px;overflow:hidden}
body{position:relative;background:var(--white);font-family:"Open Sans",Arial,sans-serif;color:var(--text);font-size:13px;line-height:1.6}
.abs{position:absolute}

/* header */
.site-header{left:0;top:0;width:1200px;height:118px}
.brand{left:99px;top:22px}
.brand-name{font-weight:700;font-size:36px;color:var(--navy);line-height:1;letter-spacing:-.5px}
.brand-tag{font-size:12.5px;color:#555;margin-top:10px}
.header-tools{right:99px;top:48px;display:flex;align-items:center;gap:26px;font-size:12.5px;color:#444}
.search-btn{width:36px;height:36px;border-radius:50%;background:#e8e8e8;display:flex;align-items:center;justify-content:center}
.login-btn{background:var(--orange);color:#fff;font-weight:700;font-size:13px;padding:8px 30px;border-radius:2px}

/* nav */
.main-nav{left:0;top:118px;width:1200px;height:54px;background:var(--navy)}
.main-nav ul{list-style:none;display:flex;margin-left:99px;height:54px}
.main-nav li{color:#fff;font-family:"Montserrat",sans-serif;font-weight:600;font-size:15px;padding:0 24px;display:flex;align-items:center;border-right:1px solid rgba(255,255,255,.12)}
.main-nav li.active{background:var(--navy-dark)}

/* hero */
.hero{left:0;top:172px;width:1200px;height:427px;background:linear-gradient(100deg,#5b6470 0%,#9aa0a6 35%,#d9d6cf 55%,#8a8a88 80%,#4a4d52 100%)}
.hero-copy{left:133px;top:345px;color:#fff}
.hero-copy h1{font-family:"Montserrat",sans-serif;font-size:30px;font-weight:700;letter-spacing:.5px}
.hero-copy p{font-size:21px;line-height:1.4;width:500px;margin-top:4px}
.hero-dots{left:572px;top:556px;display:flex;gap:8px}
.hero-dots span{width:10px;height:10px;border-radius:50%;background:rgba(255,255,255,.6)}
.hero-dots span.on{background:var(--orange)}

/* section titles */
.section-title{font-family:"Montserrat",sans-serif;font-weight:700;font-size:15px;color:var(--navy);border-bottom:1px solid var(--line);padding-bottom:14px}
.slider-arrows{display:flex;gap:4px}
.slider-arrows span{width:26px;height:26px;border:1px solid var(--line);display:flex;align-items:center;justify-content:center;color:#aaa;font-size:12px}

/* tips grid */
.tip{width:217px}
.photo{display:block}
.tip .photo{width:217px;height:141px}
.tip h3{font-family:"Montserrat",sans-serif;font-size:11.5px;font-weight:700;color:var(--ink);margin-top:16px;line-height:1.5}
.tip p{font-size:11.5px;margin-top:8px;line-height:1.7}

.banner-ad{left:148px;top:1306px;width:623px;height:76px;background:linear-gradient(90deg,#f29a1d,#f7c36a 40%,#e9ecef 60%,#c9d3de)}

/* events */
.event{left:99px;width:714px;height:222px;border-bottom:1px solid var(--line)}
.event .photo{position:absolute;left:0;top:0;width:217px;height:158px}
.event-body{position:absolute;left:248px;top:0;width:466px}
.event-body h3{font-family:"Montserrat",sans-serif;font-size:12.5px;font-weight:700;color:var(--ink)}
.meta{display:flex;gap:18px;font-size:10px;color:#999;margin:8px 0 6px}
.event-body p{font-size:11.5px;line-height:1.9}

.pagination{left:425px;top:2565px;display:flex;gap:6px}
.pagination span{border:1px solid var(--line);font-size:11px;color:#444;padding:3px 9px;background:#f7f7f7}

/* news */
.news{width:333px}
.news h3{font-family:"Montserrat",sans-serif;font-size:13.5px;font-weight:700;color:var(--ink);line-height:1.5;width:280px}
.news .rule{width:56px;height:3px;background:var(--orange);margin:12px 0 14px}
.news p{font-size:12px;line-height:1.85}

/* sidebar */
.promo{left:845px;width:256px;height:128px;background:var(--navy);color:#fff;padding:22px 16px}
.promo-row{display:flex;gap:14px;align-items:center}
.promo h4{font-family:"Montserrat",sans-serif;font-size:13.5px;font-weight:700;line-height:1.3}
.promo p{font-size:12px;margin-top:10px;line-height:1.3}
.promo b{color:var(--orange);font-size:15px}
.side-title{left:845px;width:256px;font-family:"Montserrat",sans-serif;font-weight:700;font-size:15px;color:var(--navy);border-bottom:1px solid var(--line);padding-bottom:10px}
.connect{left:845px;top:976px;font-size:11px;color:#999}

.recent-panel{left:680px;top:998px;width:468px;height:266px;background:var(--navy);padding:28px 24px;display:grid;grid-template-columns:1fr 1fr;row-gap:22px;column-gap:30px;box-shadow:0 4px 12px rgba(0,0,0,.25)}
.recent{display:flex;gap:12px;color:#fff}
.recent .photo{width:56px;height:48px;flex:none;background:linear-gradient(135deg,#7f9bb8,#3f5f82)}
.recent strong{font-size:9.5px;font-weight:700;display:block;line-height:1.4}
.recent span{font-size:10.5px}
.mini-pager{left:852px;top:1272px;display:flex;gap:6px}
.mini-pager span{width:24px;height:24px;border:1px solid var(--line)}
.mini-pager span.on{background:#b9c08b}

.side-card{left:845px;width:256px;color:#fff}
.side-card .photo{width:256px;height:239px}
.side-card .cap{position:absolute;left:0;bottom:0;width:100%;background:rgba(28,63,103,.92);padding:12px 18px}
.side-card h5{font-family:"Montserrat",sans-serif;font-size:12px;font-weight:700}
.side-card small{font-size:11px}

.video-grid{left:845px;top:2139px;width:256px;display:grid;grid-template-columns:1fr 1fr;gap:10px}
.video{height:88px;background:linear-gradient(135deg,#8aa1b8,#44617f);position:relative}
.video svg{position:absolute;left:49px;top:28px}
.more-btn{left:845px;top:2457px;background:var(--orange);color:#fff;font-size:10px;font-weight:700;padding:9px 22px}

.tweets{left:845px;top:2518px;width:256px;height:427px;border:1px solid #ddd;background:#fff}
.tweets-head{display:flex;justify-content:space-between;padding:10px 12px;border-bottom:1px solid #ddd;font-family:"Montserrat",sans-serif;font-weight:700;font-size:14px;color:#222}
.follow-pill{font-family:"Open Sans",sans-serif;font-size:10px;font-weight:600;border:1px solid #ccc;border-radius:3px;padding:1px 8px;color:#555;background:#f2f2f2}
.tweet{display:flex;gap:12px;padding:14px 12px 10px;border-bottom:1px solid #eee;height:86px}
.tweet .avatar{width:62px;height:60px;background:var(--orange);flex:none}
.tweet p{font-size:10.5px;line-height:1.35;color:#444}
.tweet p b{color:#222}
.tweet-actions{display:flex;gap:10px;justify-content:flex-end;margin-top:6px;font-size:11px}
.tweet-box{margin:8px 10px;border:1px solid #ddd;font-size:10px;color:#aaa;padding:4px 8px}
.side-ad{left:845px;top:3001px;width:256px;height:215px;background:linear-gradient(160deg,#2a63b5,#6aa2e2 55%,#f3c02b)}
.host-ad{left:845px;top:1848px;width:256px;height:217px;background:linear-gradient(180deg,#1e4ea0,#3e78c8 45%,#e8edf4)}

/* footer */
.site-footer{left:0;top:3356px;width:1200px;height:266px;background:linear-gradient(180deg,var(--navy) 0%,#1d4777 100%);color:#fff}
.footer-col{position:absolute;top:56px}
.footer-col h4{font-family:"Montserrat",sans-serif;font-size:22px;font-weight:400;margin-bottom:12px}
.footer-col li{list-style:none;font-size:12.5px;line-height:1.75;color:#dfe6ee}
.footer-col p{font-size:12.5px;color:#dfe6ee}
.email-field{width:264px;height:34px;background:#fff;margin-top:10px;color:#999;font-size:12px;padding:8px 30px}
.subscribe-btn{margin-top:12px;background:var(--orange);width:120px;height:38px;display:flex;align-items:center;justify-content:center;font-size:14px}
.foot-news p{font-size:11.5px;line-height:1.5;margin-bottom:12px}
.footer-bar{left:0;top:3622px;width:1200px;height:74px;background:var(--navy-deep);color:#9fb0c3;font-size:12px;padding:26px 108px}
</style>
</head>
<body>

<header class="abs site-header">
  <div class="abs brand">
    <div class="brand-name">Kestrel Events</div>
    <div class="brand-tag">We are an online diary/calendar and a resource for networking events</div>
  </div>
  <div class="abs header-tools">
    <span class="search-btn"><svg width="14" height="14" viewBox="0 0 14 14"><circle cx="6" cy="6" r="4.5" fill="none" stroke="#888" stroke-width="1.6"/><line x1="9.3" y1="9.3" x2="13" y2="13" stroke="#888" stroke-width="1.6"/></svg></span>
    <span>Subscribe to our Weekly Bulletin</span>
    <span>Register to Add Events</span>
    <span class="login-btn">LOGIN</span>
  </div>
</header>

<nav class="abs main-nav">
  <ul>
    <li class="active">HOME</li><li>LATEST NEWS</li><li>UPCOMING EVENT</li><li>OUR DIARY</li><li>CALENDAR</li><li>BLOG</li><li>CONTACT</li>
  </ul>
</nav>

<section class="abs hero" role="img" aria-label="Busy city street with people walking"></section>
<div class="abs hero-copy">
  <h1>WELCOME TO KESTREL EVENTS</h1>
  <p>We are an online diary/calendar and a resource for networking events</p>
</div>
<div class="abs hero-dots"><span class="on"></span><span></span><span></span></div>

<div class="abs section-title" style="left:99px;top:638px;width:714px;display:flex;justify-content:space-between;align-items:center">
  <span>NETWORKING TIPS</span>
  <span class="slider-arrows"><span>&#8249;</span><span>&#8250;</span></span>
</div>

<article class="abs tip" style="left:99px;top:702px"><span class="photo" role="img" aria-label="City square with crowds" style="background:linear-gradient(180deg,#c9ccd0,#6f6a64)"></span><h3>LOREM IPSUM IS SIMPLY DUMMY TEXT OF THE PRINTING</h3><p>Lorem Ipsum is simply dummy text of the printing and typesetting industry. been the industry's...</p></article>
<article class="abs tip" style="left:347px;top:702px"><span class="photo" role="img" aria-label="Silhouette standing on a pier" style="background:linear-gradient(180deg,#e6e6e6,#3a3a3a)"></span><h3>LOREM IPSUM IS SIMPLY DUMMY TEXT OF THE PRINTING</h3><p>Lorem Ipsum is simply dummy text of the printing and typesetting industry. been the industry's...</p></article>
<article class="abs tip" style="left:596px;top:702px"><span class="photo" role="img" aria-label="Airport terminal interior" style="background:linear-gradient(180deg,#d8d8d8,#555)"></span><h3>LOREM IPSUM IS SIMPLY DUMMY TEXT OF THE PRINTING</h3><p>Lorem Ipsum is simply dummy text of the printing and typesetting industry. been the industry's...</p></article>
<article class="abs tip" style="left:99px;top:998px"><span class="photo" role="img" aria-label="Car dashboard on a road" style="background:linear-gradient(180deg,#a9b7c4,#2e2e2e)"></span><h3>LOREM IPSUM IS SIMPLY DUMMY TEXT OF THE PRINTING</h3><p>Lorem Ipsum is simply dummy text of the printing and typesetting industry. been the industry's...</p></article>
<article class="abs tip" style="left:347px;top:998px"><span class="photo" role="img" aria-label="Airliner in a blue sky" style="background:linear-gradient(180deg,#3f6fa8,#b5cbe0)"></span><h3>LOREM IPSUM IS SIMPLY DUMMY TEXT OF THE PRINTING</h3><p>Lorem Ipsum is simply dummy text of the printing and typesetting industry. been the industry's...</p></article>
<article class="abs tip" style="left:596px;top:998px"><span class="photo" role="img" aria-label="World map" style="background:linear-gradient(180deg,#8a6a44,#3a3f4a)"></span><h3>LOREM IPSUM IS SIMPLY DUMMY TEXT OF THE PRINTING</h3><p>Lorem Ipsum is simply dummy text of the printing and typesetting industry. been the industry's...</p></article>

<div class="abs banner-ad" role="img" aria-label="Advertisement banner for free video tutorials"></div>

<div class="abs section-title" style="left:99px;top:1416px;width:714px">UPCOMING EVENTS</div>

<article class="abs event" style="top:1488px"><span class="photo" role="img" aria-label="Canal with old buildings" style="background:linear-gradient(180deg,#8fb2d4,#a87a52)"></span><div class="event-body"><h3>LOREM IPSUM IS SIMPLY DUMMY EXT OF THE PRINTING</h3><div class="meta"><span>&#9719; 27 MARCH 2015</span><span>&#9825; 108</span><span>&#9993; 265</span></div><p>Lorem Ipsum is simply dummy text of the printing and typesetting industry. Lorem Ipsum has been the industry's standard dummy text ever since the 1500s, when an unknown printer took a galley of type and scrambled it to make a type specimen book. It has survived not only five centuries, but also the leap...</p></div></article>
<article class="abs event" style="top:1710px"><span class="photo" role="img" aria-label="High speed train in motion" style="background:linear-gradient(135deg,#d5d9de,#6d4c3a)"></span><div class="event-body"><h3>LOREM IPSUM IS SIMPLY DUMMY EXT OF THE PRINTING</h3><div class="meta"><span>&#9719; 27 MARCH 2015</span><span>&#9825; 108</span><span>&#9993; 265</span></div><p>Lorem Ipsum is simply dummy text of the printing and typesetting industry. Lorem Ipsum has been the industry's standard dummy text ever since the 1500s, when an unknown printer took a galley of type and scrambled it to make a type specimen book. It has survived not only five centuries, but also the leap...</p></div></article>
<article class="abs event" style="top:1932px"><span class="photo" role="img" aria-label="Colleagues meeting at a laptop" style="background:linear-gradient(135deg,#b9b2a6,#6a6e75)"></span><div class="event-body"><h3>LOREM IPSUM IS SIMPLY DUMMY EXT OF THE PRINTING</h3><div class="meta"><span>&#9719; 27 MARCH 2015</span><span>&#9825; 108</span><span>&#9993; 265</span></div><p>Lorem Ipsum is simply dummy text of the printing and typesetting industry. Lorem Ipsum has been the industry's standard dummy text ever since the 1500s, when an unknown printer took a galley of type and scrambled it to make a type specimen book. It has survived not only five centuries, but also the leap...</p></div></article>
<article class="abs event" style="top:2154px"><span class="photo" role="img" aria-label="Two people talking outdoors" style="background:linear-gradient(135deg,#7d96b6,#3b3a45)"></span><div class="event-body"><h3>LOREM IPSUM IS SIMPLY DUMMY EXT OF THE PRINTING</h3><div class="meta"><span>&#9719; 27 MARCH 2015</span><span>&#9825; 108</span><span>&#9993; 265</span></div><p>Lorem Ipsum is simply dummy text of the printing and typesetting industry. Lorem Ipsum has been the industry's standard dummy text ever since the 1500s, when an unknown printer took a galley of type and scrambled it to make a type specimen book. It has survived not only five centuries, but also the leap...</p></div></article>
<article class="abs event" style="top:2376px;border-bottom:none"><span class="photo" role="img" aria-label="Man with glasses and bow tie" style="background:linear-gradient(135deg,#e7e2d8,#b23a2a)"></span><div class="event-body"><h3>LOREM IPSUM IS SIMPLY DUMMY EXT OF THE PRINTING</h3><div class="meta"><span>&#9719; 27 MARCH 2015</span><span>&#9825; 108</span><span>&#9993; 265</span></div><p>Lorem Ipsum is simply dummy text of the printing and typesetting industry. Lorem Ipsum has been the industry's standard dummy text ever since the 1500s, when an unknown printer took a galley of type and scrambled it to make a type specimen book. It has survived not only five centuries, but also the leap...</p></div></article>

<div class="abs pagination"><span>Prev</span><span>1</span><span>2</span><span>3</span><span>4</span><span>5</span><span>6</span><span>...</span><span>22</span><span>Next</span></div>

<div class="abs section-title" style="left:99px;top:2638px;width:714px">NETWORKING NEWS</div>
<article class="abs news" style="left:99px;top:2706px"><h3>LOREM IPSUM IS SIMPLY DUMMY EXT OF THE PRINTING</h3><div class="rule"></div><p>Lorem Ipsum is simply dummy text of the printing and typesetting industry. Lorem Ipsum has been the industry's standard dummy text ever since the 1500s, when an unknown printer took a galley...</p></article>
<article class="abs news" style="left:480px;top:2706px"><h3>LOREM IPSUM IS SIMPLY DUMMY EXT OF THE PRINTING</h3><div class="rule"></div><p>Lorem Ipsum is simply dummy text of the printing and typesetting industry. Lorem Ipsum has been the industry's standard dummy text ever since the 1500s, when an unknown printer took a galley...</p></article>
<article class="abs news" style="left:99px;top:2918px"><h3>LOREM IPSUM IS SIMPLY DUMMY EXT OF THE PRINTING</h3><div class="rule"></div><p>Lorem Ipsum is simply dummy text of the printing and typesetting industry. Lorem Ipsum has been the industry's standard dummy text ever since the 1500s, when an unknown printer took a galley...</p></article>
<article class="abs news" style="left:480px;top:2918px"><h3>LOREM IPSUM IS SIMPLY DUMMY EXT OF THE PRINTING</h3><div class="rule"></div><p>Lorem Ipsum is simply dummy text of the printing and typesetting industry. Lorem Ipsum has been the industry's standard dummy text ever since the 1500s, when an unknown printer took a galley...</p></article>
<article class="abs news" style="left:99px;top:3124px"><h3>LOREM IPSUM IS SIMPLY DUMMY EXT OF THE PRINTING</h3><div class="rule"></div><p>Lorem Ipsum is simply dummy text of the printing and typesetting industry. Lorem Ipsum has been the industry's standard dummy text ever since the 1500s, when an unknown printer took a galley...</p></article>
<article class="abs news" style="left:480px;top:3124px"><h3>LOREM IPSUM IS SIMPLY DUMMY EXT OF THE PRINTING</h3><div class="rule"></div><p>Lorem Ipsum is simply dummy text of the printing and typesetting industry. Lorem Ipsum has been the industry's standard dummy text ever since the 1500s, when an unknown printer took a galley...</p></article>

<aside>
  <div class="abs promo" style="top:641px">
    <div class="promo-row"><svg width="34" height="30" viewBox="0 0 34 30"><circle cx="17" cy="9" r="6" fill="none" stroke="#f6a11a" stroke-width="2"/><path d="M5 29c0-7 5-11 12-11s12 4 12 11" fill="none" stroke="#f6a11a" stroke-width="2"/></svg><h4>COMMUNITY<br>EVENTS</h4></div>
    <p>community events and one off events would be <b>FREE</b></p>
  </div>
  <div class="abs promo" style="top:788px">
    <div class="promo-row"><svg width="34" height="30" viewBox="0 0 34 30"><rect x="4" y="6" width="12" height="23" fill="none" stroke="#f6a11a" stroke-width="2"/><rect x="18" y="12" width="12" height="17" fill="none" stroke="#f6a11a" stroke-width="2"/></svg><h4>BUSINESS AND<br>COMMERCIAL EVENTS</h4></div>
    <p>would be <b>CHARGEABLE</b></p>
  </div>

  <div class="abs side-title" style="top:940px">FOLLOW US</div>
  <div class="abs connect">Connect with our social media</div>

  <div class="abs recent-panel">
    <div class="recent"><span class="photo" role="img" aria-label="Event thumbnail"></span><div><strong>LOREM IPSUM IS SIMPLY DUMMY</strong><span>On 30 november 2015</span></div></div>
    <div class="recent"><span class="photo" role="img" aria-label="Event thumbnail"></span><div><strong>LOREM IPSUM IS SIMPLY DUMMY</strong><span>On 30 november 2015</span></div></div>
    <div class="recent"><span class="photo" role="img" aria-label="Event thumbnail"></span><div><strong>LOREM IPSUM IS SIMPLY DUMMY</strong><span>On 30 november 2015</span></div></div>
    <div class="recent"><span class="photo" role="img" aria-label="Event thumbnail"></span><div><strong>LOREM IPSUM IS SIMPLY DUMMY</strong><span>On 30 november 2015</span></div></div>
    <div class="recent"><span class="photo" role="img" aria-label="Event thumbnail"></span><div><strong>LOREM IPSUM IS SIMPLY DUMMY</strong><span>On 30 november 2015</span></div></div>
    <div class="recent"><span class="photo" role="img" aria-label="Event thumbnail"></span><div><strong>LOREM IPSUM IS SIMPLY DUMMY</strong><span>On 30 november 2015</span></div></div>
  </div>
  <div class="abs mini-pager"><span></span><span class="on"></span><span></span><span></span><span></span></div>

  <div class="abs side-card" style="top:1338px;height:239px"><span class="photo" role="img" aria-label="Business people at a laptop" style="background:linear-gradient(135deg,#dfe6ee,#7b8ea3)"></span><div class="cap"><h5>SUBSCRIBE</h5><small>Subscribe to our event &#187;</small></div></div>
  <div class="abs side-card" style="top:1597px;height:226px"><span class="photo" role="img" aria-label="Smiling woman at a desk" style="height:226px;background:linear-gradient(135deg,#f1f1f1,#a9a39b)"></span><div class="cap"><h5>REGISTER</h5><small>Register to Add Events &#187;</small></div></div>

  <div class="abs host-ad" role="img" aria-label="Advertisement for web hosting servers"></div>

  <div class="abs side-title" style="top:2092px">VIDEO GALLERY</div>
  <div class="abs video-grid">
    <div class="video" role="img" aria-label="Video thumbnail"><svg width="30" height="30" viewBox="0 0 30 30"><circle cx="15" cy="15" r="14" fill="rgba(255,255,255,.85)"/><path d="M12 9l9 6-9 6z" fill="#1c3f67"/></svg></div>
    <div class="video" role="img" aria-label="Video thumbnail"><svg width="30" height="30" viewBox="0 0 30 30"><circle cx="15" cy="15" r="14" fill="rgba(255,255,255,.85)"/><path d="M12 9l9 6-9 6z" fill="#1c3f67"/></svg></div>
    <div class="video" role="img" aria-label="Video thumbnail"><svg width="30" height="30" viewBox="0 0 30 30"><circle cx="15" cy="15" r="14" fill="rgba(255,255,255,.85)"/><path d="M12 9l9 6-9 6z" fill="#1c3f67"/></svg></div>
    <div class="video" role="img" aria-label="Video thumbnail"><svg width="30" height="30" viewBox="0 0 30 30"><circle cx="15" cy="15" r="14" fill="rgba(255,255,255,.85)"/><path d="M12 9l9 6-9 6z" fill="#1c3f67"/></svg></div>
    <div class="video" role="img" aria-label="Video thumbnail"><svg width="30" height="30" viewBox="0 0 30 30"><circle cx="15" cy="15" r="14" fill="rgba(255,255,255,.85)"/><path d="M12 9l9 6-9 6z" fill="#1c3f67"/></svg></div>
    <div class="video" role="img" aria-label="Video thumbnail"><svg width="30" height="30" viewBox="0 0 30 30"><circle cx="15" cy="15" r="14" fill="rgba(255,255,255,.85)"/><path d="M12 9l9 6-9 6z" fill="#1c3f67"/></svg></div>
  </div>
  <div class="abs more-btn">VIEW MORE VIDEOS</div>

  <div class="abs tweets">
    <div class="tweets-head"><span>Tweets</span><span class="follow-pill">Follow</span></div>
    <div class="tweet"><span class="avatar"></span><div><p><b>Lorem Ipsum is simply</b> dummy text of the printing and typesetting...</p><div class="tweet-actions"><span>&#8617;</span><span>&#8646;</span><span>&#9733;</span></div></div></div>
    <div class="tweet"><span class="avatar"></span><div><p><b>Lorem Ipsum is simply</b> dummy text of the printing and typesetting...</p><div class="tweet-actions"><span>&#8617;</span><span>&#8646;</span><span>&#9733;</span></div></div></div>
    <div class="tweet"><span class="avatar"></span><div><p><b>Lorem Ipsum is simply</b> dummy text of the printing and typesetting...</p><div class="tweet-actions"><span>&#8617;</span><span>&#8646;</span><span>&#9733;</span></div></div></div>
    <div class="tweet"><span class="avatar"></span><div><p><b>Lorem Ipsum is simply</b> dummy text of the printing and typesetting...</p><div class="tweet-actions"><span>&#8617;</span><span>&#8646;</span><span>&#9733;</span></div></div></div>
    <div class="tweet-box">Tweet to @kestrelevents</div>
  </div>

  <div class="abs side-ad" role="img" aria-label="Advertisement for family domain hosting"></div>
</aside>

<footer class="abs site-footer">
  <div class="footer-col" style="left:108px">
    <h4>Quick links</h4>
    <ul><li>About Us</li><li>What We Do</li><li>How we work</li><li>Blog Post</li><li>News &amp; Events</li></ul>
  </div>
  <div class="footer-col" style="left:335px">
    <h4>Resources</h4>
    <ul><li>Mauris vel lacus</li><li>Vitae felis vestibulum</li><li>Aolutpat imperdiet</li><li>Cum sociis</li><li>Natoque penatibus</li></ul>
  </div>
  <div class="footer-col" style="left:537px">
    <h4>Newsletters Sign Up</h4>
    <p>Please sign up here for latest news</p>
    <div class="email-field">Email address</div>
    <div class="subscribe-btn">Subscribe</div>
  </div>
  <div class="footer-col foot-news" style="left:855px;width:240px">
    <h4 style="display:flex;justify-content:space-between">Follow Us <span style="font-size:16px">&#8249; &#8250;</span></h4>
    <p>Lorem Ipsum is simply dummy text of the printing, from our print partner</p>
    <p>Lorem Ipsum is simply dummy text of the printing, from our print partner</p>
    <p>Lorem Ipsum is simply dummy text of the printing, from our print partner</p>
  </div>
</footer>
<div class="abs footer-bar">© 2015 Company Name All right reserved Term of Use</div>

</body>
</html>
```